Soft furnishing company selling fabrics, curtains, bedlinen craft & haberdashery

We need 4 x home page banners for our website as follows:
Image 1 - to lead customers to our "New season Fabrics" page,
Image 2 - to lead customers to our Ready Made curtains,
Image 3 - to lead customers to our "Polar Bear Bed linen" page
Image 4 - to lead customers to our "Christmas raft Tutorial" page

Banner needs to be 960px wide x 380px 72dpi and optimised for web. should have a little descriptive text for example "Fabulous Fabric. Prints, plains & weaves, view our range of new season furnishing fabrics to buy by the metre" "Instantly update your home with our range of ready made curtains. Available . "Cosy Night In. Snuggle with this Polar Bear Duvet Set. From €20" "" "Let's Get Crafting for Christmas. Download our free Project and tutoirals here. First 3 images need a "shop now" button

website url www.lintelway.ie

Target Market(s)

Female 25 -45

Industry/Entity Type

It Company

Font styles to use
Serif
Sans Serif

Requirements
Must have
• shop now button on image 1, 2, 3
Should not have
• too much text or clutter

```html
<!DOCTYPE html>
<html lang="en">
<head>
<meta charset="utf-8">
<title>Lintelway Home Page Banners</title>
<link href="https://fonts.googleapis.com/css2?family=Playfair+Display:wght@400;700&family=Courier+Prime:wght@700&family=Open+Sans:wght@400;600&display=swap" rel="stylesheet">
<style>
  :root {
    --page: #ffffff;
    --white: #ffffff;
    --ink: #2b2b2b;
    --grey-text: #555555;
    --orange: #f0a13a;
    --red: #d9232e;
    --button-bg: #1c1c1c;
    --serif: "Playfair Display", Georgia, serif;
    --slab: "Courier Prime", "Courier New", monospace;
    --sans: "Open Sans", Arial, sans-serif;
  }
  * { box-sizing: border-box; margin: 0; padding: 0; }
  html, body { width: 727px; height: 1200px; overflow: hidden; background: var(--page); }
  .banner-stack { position: relative; width: 727px; height: 1200px; }
  .banner { position: absolute; left: 12px; width: 703px; overflow: hidden; }
  .banner-fabric { top: 12px; height: 274px; }
  .banner-curtains { top: 310px; height: 271px; }
  .banner-bedlinen { top: 600px; height: 271px; }
  .banner-craft { top: 900px; height: 274px; border: 2px solid var(--red); background: var(--white); }

  .photo { position: absolute; inset: 0; }
  .photo-fabric {
    background:
      linear-gradient(90deg, rgba(0,0,0,0) 40%, rgba(20,12,8,.85) 70%, rgba(15,10,6,.92) 100%),
      linear-gradient(180deg, #c8a98a 0%, #9b7457 35%, #6b4a35 60%, #b88a5a 80%, #7a5230 100%);
  }
  .photo-curtains {
    background:
      linear-gradient(180deg, rgba(0,0,0,0) 55%, rgba(0,0,0,.75) 100%),
      linear-gradient(90deg, #5a2a26 0%, #7c3a30 25%, #4b3a35 45%, #8a6c55 60%, #6e3a2e 80%, #3a2c26 100%);
  }
  .photo-bedlinen {
    background:
      radial-gradient(ellipse at 20% 55%, #e8e6e2 0%, #cfcdc8 30%, rgba(160,158,154,0) 55%),
      linear-gradient(90deg, #9a9893 0%, #7e7c78 45%, #8d8b87 100%);
  }
  .photo-craft {
    position: absolute; left: 340px; top: 30px; width: 350px; height: 220px;
    background: radial-gradient(ellipse at 55% 55%, #f6e2e2 0%, #f0c8c8 35%, rgba(255,255,255,0) 70%);
  }

  .title { font-family: var(--serif); font-weight: 700; color: var(--white); line-height: 1; white-space: nowrap; }
  .tagline { font-family: var(--slab); color: var(--orange); font-weight: 700; white-space: nowrap; }
  .copy { font-family: var(--sans); color: var(--white); font-size: 16px; line-height: 1.3; }

  .shop-button {
    display: inline-flex; align-items: center; gap: 8px;
    font-family: var(--sans); font-weight: 600; font-size: 14px; letter-spacing: .5px;
    color: var(--white); background: var(--button-bg);
    border: 2px solid var(--white); padding: 4px 10px; text-transform: uppercase;
  }
  .shop-button svg { width: 10px; height: 12px; fill: var(--white); }

  .fabric-text { position: absolute; right: 14px; top: 18px; width: 400px; text-align: right; }
  .fabric-text .title { font-size: 46px; }
  .fabric-text .tagline { font-size: 25px; margin-top: 6px; }
  .fabric-text .copy { margin-top: 12px; font-size: 15.5px; }
  .fabric-text .shop-button { position: absolute; right: 4px; top: 170px; }

  .curtains-text { position: absolute; left: 14px; top: 140px; }
  .curtains-text .title { font-size: 46px; }
  .curtains-row { display: flex; align-items: center; gap: 12px; }
  .curtains-text .copy { margin-top: 8px; font-size: 15.5px; }

  .bedlinen-text { position: absolute; right: 14px; top: 14px; width: 500px; text-align: right; }
  .bedlinen-text .title { font-size: 44px; }
  .bedlinen-text .tagline { font-size: 25px; margin-top: 16px; }
  .bedlinen-text .copy { margin-top: 8px; font-size: 16px; }
  .bedlinen-text .shop-button { position: absolute; right: 4px; top: 196px; }

  .craft-text { position: absolute; left: 16px; top: 18px; width: 460px; }
  .craft-text .title { color: var(--red); font-weight: 400; font-size: 48px; line-height: 1.02; }
  .craft-text .copy { color: var(--grey-text); margin-top: 14px; font-size: 16px; }
  .view-button {
    display: inline-flex; align-items: center; gap: 8px; margin-top: 14px;
    font-family: var(--sans); font-size: 14px; font-weight: 600; color: var(--red);
    border: 1.5px solid var(--red); padding: 4px 10px; letter-spacing: .5px;
  }
  .view-button svg { width: 10px; height: 12px; fill: var(--red); }
</style>
</head>
<body>
<main class="banner-stack">

  <section class="banner banner-fabric">
    <div class="photo photo-fabric" role="img" aria-label="Stacked rolls of patterned furnishing fabric with autumn leaves scattered in front"></div>
    <div class="fabric-text">
      <h2 class="title">Fabulous Fabric</h2>
      <p class="tagline">Prints, Plains &amp; Weaves</p>
      <p class="copy">View our range of new season<br>furnishing fabrics to buy by the metre</p>
      <span class="shop-button">Shop now <svg viewBox="0 0 10 12"><path d="M0 0 L10 6 L0 12 Z"/></svg></span>
    </div>
  </section>

  <section class="banner banner-curtains">
    <div class="photo photo-curtains" role="img" aria-label="Living room with tartan ready made curtains and a checked armchair"></div>
    <div class="curtains-text">
      <h2 class="title">Ready Made</h2>
      <div class="curtains-row">
        <span class="title">Curtains</span>
        <span class="shop-button">Shop now <svg viewBox="0 0 10 12"><path d="M0 0 L10 6 L0 12 Z"/></svg></span>
      </div>
      <p class="copy">Instantly update your home with our range of ready made curtains</p>
    </div>
  </section>

  <section class="banner banner-bedlinen">
    <div class="photo photo-bedlinen" role="img" aria-label="Polar bear print cushion on a soft grey faux fur throw"></div>
    <div class="bedlinen-text">
      <h2 class="title">Polar Bear Bed Linen</h2>
      <p class="tagline">Cosy Night In?</p>
      <p class="copy">Snuggle with this Polar Bear<br>Duvet Set. From €20</p>
      <span class="shop-button">Shop now <svg viewBox="0 0 10 12"><path d="M0 0 L10 6 L0 12 Z"/></svg></span>
    </div>
  </section>

  <section class="banner banner-craft">
    <div class="photo-craft" role="img" aria-label="Handmade fabric reindeer pulling a red patterned fabric sleigh"></div>
    <div class="craft-text">
      <h2 class="title">Christmas Craft<br>Tutorials</h2>
      <p class="copy">Let's Get Crafting for Christmas.<br>Download our free Project<br>and tutoirals here.</p>
      <span class="view-button">VIEW TUTORIALS <svg viewBox="0 0 10 12"><path d="M0 0 L10 6 L0 12 Z"/></svg></span>
    </div>
  </section>

</main>
</body>
</html>
```